Neukunden-Flyer für Yoga-&Massage
Zielgruppe
Yoga-Leherin, die Yoga nicht nur zur zeitweisen Entspannung vermittelt sondern als Ansatz dauerhafter Entschleunigung, Stressbewältigung und körperlicher Fitness. Thai Yoga Massage arbeitet nicht nur körperlich sondern auch energetisch auch auf der Herzebene.
Zielgruppe:
Jeder, der sich etwas Gutes tun will und seine Selbstheilungskräfte aktivieren und wieder mehr bei sich sein möchte.
Aufgabenstellung
Erstellung eines Flyers mit folgenden Eigenschaften:
• DIN A4 lang - Wickelfalz-Flyer 6-seitig
• Klare Formen und kräftige Farben
• Einprägsam
• Fließend
• CMYK - keine Sonderfarben
• Druckdatenvorlage (PSDs (außen/innen bzw. Druckdatenerstellung Fonts/Pfade
beachten)
Abgabe als offene Datei: PSD, AI bzw. als geschlossene Druckdatei X3 PDF.

```html
<!DOCTYPE html>
<html lang="de">
<head>
<meta charset="utf-8">
<title>ATEMRAUM – Wickelfalz-Flyer</title>
<link href="https://fonts.googleapis.com/css2?family=Arimo:wght@400;700&family=Open+Sans:wght@400&display=swap" rel="stylesheet">
<style>
:root{
  --pink:#e0559a;
  --pink-deep:#d9448e;
  --lime:#bccf1a;
  --lime-text:#c5d42a;
  --white:#ffffff;
  --ink:#111111;
  --sun:#f4d9b0;
  --glow:#c98b5a;
  --earth:#5a3a25;
  --dark:#2e1f16;
}
*{margin:0;padding:0;box-sizing:border-box}
html,body{width:1200px;height:1185px;overflow:hidden;background:var(--white)}
body{position:relative;font-family:"Arimo",Arial,sans-serif;color:var(--white)}
.sheet-frame{position:absolute;left:0;top:0;width:1056px;height:1184px;border-right:1px solid var(--ink);border-bottom:1px solid var(--ink)}
.sheet-label{position:absolute;font-family:"Open Sans",Arial,sans-serif;color:var(--ink);font-size:19px}
.sheet-label--outer{left:817px;top:8px}
.sheet-label--inner{left:29px;top:609px}
.panel{position:absolute;overflow:hidden}
.photo-sunset{background:radial-gradient(circle at 30% 22%,var(--sun) 0,#e7b883 14%,var(--glow) 32%,#8a5a3a 58%,var(--earth) 82%,var(--dark) 100%)}
.photo-portrait{background:radial-gradient(ellipse at 55% 75%,#e8b98e 0,#b07955 25%,transparent 50%),radial-gradient(circle at 20% 15%,#f3dcc0 0,#c99773 30%,#7a4d33 62%,#3a271b 100%)}
.panel--pink{background:linear-gradient(180deg,var(--pink) 0%,var(--pink-deep) 100%)}
.copy{position:absolute;font-size:10.3px;line-height:12.7px}
.copy p{margin-bottom:12.7px}
.accent{color:var(--lime-text);font-weight:700}
.copy-heading{color:var(--lime-text);font-weight:700;font-size:12.4px;letter-spacing:.2px}
.brand{position:absolute;left:578px;top:430px;width:190px;text-align:center}
.brand-dot{display:block;margin:0 auto 14px;width:78px;height:78px;border-radius:50%;background:var(--lime)}
.brand-name{font-size:20px;letter-spacing:4px;color:#d8c9bb;font-weight:400}
.strip-top{position:absolute;left:253px;top:614px;width:803px;height:23px;background:linear-gradient(90deg,#f2e3d0,#f7efe5 40%,#efe0cc)}
.strip-top--pink{position:absolute;left:516px;top:614px;width:271px;height:23px;background:var(--pink)}
.service-band{position:absolute;left:253px;top:637px;width:803px;height:52px;background:var(--lime);display:flex}
.service-band span{flex:0 0 auto;display:flex;align-items:center;justify-content:center;font-weight:700;font-size:15.5px;letter-spacing:.3px}
.service-band .s1{width:263px}.service-band .s2{width:271px}.service-band .s3{width:269px}
.thumb{position:absolute}
.thumb--massage{left:300px;top:721px;width:79px;height:119px;background:linear-gradient(160deg,#2a211c,#8c7b70 45%,#e6e0dc 70%,#5b4a40)}
.thumb--foot{left:384px;top:755px;width:79px;height:119px;background:linear-gradient(170deg,#d9d2c8,#e6b89a 45%,#c99277 70%,#e9e4de)}
.bold{font-weight:700}
</style>
</head>
<body>
<div class="sheet-frame"></div>
<div class="sheet-label sheet-label--outer">Aussen (Schöndruck)</div>
<div class="sheet-label sheet-label--inner">Innen (Wiederdruck)</div>

<!-- Aussenseite -->
<section class="outer">
  <div class="panel photo-sunset" role="img" aria-label="Warmes Gegenlichtfoto einer Landschaft im Sonnenuntergang" style="left:0;top:0;width:270px;height:569px"></div>
  <div class="panel panel--pink" style="left:270px;top:0;width:272px;height:569px"></div>
  <div class="panel photo-portrait" role="img" aria-label="Foto einer Frau von hinten im warmen Abendlicht" style="left:542px;top:0;width:263px;height:569px"></div>

  <div class="copy" style="left:24px;top:340px;width:215px">
    <p><span class="accent">ATEMRAUM</span><br>versteht sich als Kraftquelle<br>für körperliche Fitness, mentale Ruhe und<br>seelisches Gleichgewicht.</p>
    <p><span class="accent">Vita</span><br>800 Stunden zertifizierte Hatha Lehrerin.<br>Ausbildung bei Jonas Keller und Mira<br>Brandt. Laufende Assistenz bei Tobias<br>Lenz (Ashtanga Studio). Ich unterrichte<br>in München Gruppen- &amp; Einzelkurse – unter<br>anderem in den Yoga-Studios von Jonas<br>Keller, Yoga-Lehrer der Fußball-National-<br>mannschaft.</p>
  </div>

  <div class="copy" style="left:294px;top:94px;width:210px">
    <p class="copy-heading" style="margin-bottom:18px">TERMIN &amp; KONTAKT</p>
    <p>Vereinbaren Sie noch heute einen Termin<br>und erleben Sie, wie Sie durch individuelle<br>Körperarbeit mehr zu sich selbst finden.</p>
    <p>ATEMRAUM<br>Lena Vogt<br>Lindenweg 12<br>80331 München<br>E-Mail: info@atemraum.de<br>Mobil: 0176 - 12345678</p>
    <p>Anreise mit Auto:<br>LINDENHOF - zentral in München<br>Alt-Lindenau ggf. Rückseite finden sich fast<br>immer Parkgelegenheiten.</p>
    <p>Anreise mit MVV:<br>Die Buslinien 132, N40, N41<br>(Haltestelle Lindenplatz) sowie 63<br>(Haltestelle</p>
    <p>Marktkirche) halten direkt vor der Tür.<br>Nur 5 Minuten zu Fuß sind U3, S7 und S27<br>(Haltestelle Südbahnhof) entfernt.</p>
  </div>

  <div class="brand">
    <span class="brand-dot"></span>
    <span class="brand-name">ATEMRAUM</span>
  </div>
</section>

<!-- Innenseite -->
<section class="inner">
  <div class="strip-top"></div>
  <div class="strip-top--pink"></div>
  <div class="panel photo-sunset" role="img" aria-label="Warmes Gegenlichtfoto im Sonnenuntergang" style="left:253px;top:689px;width:263px;height:494px"></div>
  <div class="panel panel--pink" style="left:516px;top:689px;width:271px;height:494px"></div>
  <div class="panel photo-portrait" role="img" aria-label="Foto einer Frau von hinten im warmen Abendlicht" style="left:787px;top:689px;width:268px;height:494px"></div>

  <div class="service-band">
    <span class="s1">Thai Yoga Massage</span>
    <span class="s2">Yoga</span>
    <span class="s3">Coach</span>
  </div>

  <div class="thumb thumb--massage" role="img" aria-label="Foto einer Thai Yoga Massage"></div>
  <div class="thumb thumb--foot" role="img" aria-label="Foto einer Fußmassage"></div>

  <div class="copy" style="left:276px;top:887px;width:225px">
    <p class="copy-heading" style="font-size:11px;line-height:13px;margin-bottom:0">Wann haben Sie sich das letzte Mal in<br>Ihrem Körper zuhause gefühlt?</p>
    <p class="bold" style="margin-bottom:0">Thai Yoga Massage ermöglicht tiefe Rege-<br>neration. Verspannungen und Energieb-<br>lockaden werden durch nährende Berüh-<br>rungen wirkungsvoll gelöst. Die Erfahrung<br>bewegt zu werden umfasst Körper, Seele<br>und Geist. Ein Erlebnis, dass noch lange<br>nachwirkt.<br>Gönnen Sie sich einen ruhigen Raum,<br>Achtsamkeit, Präsenz, Zeit nur für sich.<br>Eine Investition um neue Energie zu<br>tanken.</p>
  </div>
  <div class="copy bold" style="left:276px;top:1096px;width:220px">
    <span class="copy-heading" style="font-size:11.5px">Preise</span><br>Schnupperpreis 60 min / 45 €<br>60 Minuten – 60 €<br>90 Minuten – 85 €<br>120 Minuten – 110 €
  </div>

  <div class="copy" style="left:543px;top:842px;width:225px;line-height:13.6px">
    <p>Der Einzelunterricht richtet sich nach Ihren<br>individuellen Zielen und Wünschen.</p>
    <p>Ihren Fähigkeiten nach, erarbeiten wir<br>ihre ganz persönliche Übungssequenz.<br>Die Atmung ist der Schlüssel zur bewuss-<br>ten Wahrnehmung.</p>
    <p>Steigerung des körperlichen Wohlbefin-<br>dens, Ausgeglichenheit und Widerstands-<br>fähigkeit sind die Folge.</p>
    <p>Jede Stunde endet mit einer 5-minütigen<br>Nackenmassage und anschließender<br>Tiefenentspannung.</p>
  </div>
  <div class="copy bold" style="left:538px;top:1096px;width:220px">
    <span class="copy-heading" style="font-size:11.5px">Preise</span><br>Schnupperpreis 60 min / 55 €<br>60 Minuten – 85 €<br>90 Minuten – 110 €
  </div>

  <div class="copy" style="left:815px;top:957px;width:225px;line-height:13.6px">
    <p>Im Coaching lernen Sie mit beruflichen<br>Konflikten und persönlichen Beziehungs-<br>spannungen umzugehen.<br>Ich gebe Ihnen alltagstaugliche Techniken<br>an die Hand um sich für die persönlichen<br>Herausforderungen zu stärken und immer<br>wieder tiefe Ruhepole zu finden.</p>
  </div>
  <div class="copy bold" style="left:814px;top:1096px;width:220px">
    <span class="copy-heading" style="font-size:11.5px">Preise</span><br>Schnupperpreis 60 min / 55 €<br>60 Minuten – 85 €<br>90 Minuten – 110 €
  </div>
</section>
</body>
</html>
```